Therapy Services & Training

I provide counseling/therapy to individuals and families. I also travel the country and provide training at conferences.
I would like to see a card which takes my company name and design a logo using the letters "MCAC".
Target Market(s)
Therapists, non-profit organizations, clients looking for therapy
Industry/Entity Type
Training
Contact Information for Business Card
Meridel Clinical Advising & Coaching LLC
Danelle Brooks, M.S.W., LCSW
Clinical Therapist & Trainer
Providing clinical therapy services to individuals, families, couples & children. We also provide life coaching and crisis training.
helpdeskdanelle@mailbrook.example
www.meridelclinicaladvising.example
(555) 214-0397
Halden, IL 60400
(BACK SIDE OF CARD)
We are certified by the Baseline Ongoing Lawyer Instruction (BOLI) Panel of the Statewide High Tribunal to provide Continuing Legal Education (CLE) credits to Illinois attorneys. Call about what courses we offer! (555) 214-0397

```html
<!DOCTYPE html>
<html lang="en">
<head>
<meta charset="utf-8">
<title>Meridel Clinical Advising &amp; Coaching — Business Card</title>
<link rel="stylesheet" href="https://fonts.googleapis.com/css2?family=Jost:wght@300;400;500;600&display=swap">
<style>
  :root {
    --backdrop: #c9d3d3;
    --card: #ffffff;
    --ink: #1a1a1a;
    --ink-soft: #333333;
    --name-blue: #2a12e6;
    --contact-blue: #3a8cf0;
    --mark-violet: #2f14e0;
    --mark-lilac: #b79cf0;
    --mark-sky: #3b93f7;
  }
  * { box-sizing: border-box; margin: 0; padding: 0; }
  html, body {
    width: 1200px; height: 1000px; overflow: hidden;
    background: var(--backdrop);
    font-family: "Jost", "Futura", sans-serif;
    color: var(--ink);
  }
  .canvas { position: relative; width: 1200px; height: 1000px; }
  .card {
    position: absolute;
    width: 800px;
    background: var(--card);
    box-shadow: 0 6px 18px rgba(0,0,0,0.18);
  }

  /* Back side */
  .card--back { left: 60px; top: 30px; height: 450px; }
  .back-statement {
    position: absolute; left: 50px; top: 90px; width: 470px;
    font-weight: 300; font-size: 18px; line-height: 30px; color: var(--ink-soft);
  }
  .back-call {
    position: absolute; left: 50px; top: 300px;
    font-weight: 300; font-size: 18px; color: var(--ink-soft);
  }

  /* Brand stand-in */
  .brand {
    position: absolute; display: flex; align-items: center; gap: 14px;
  }
  .brand-dot {
    width: 34px; height: 34px; border-radius: 50%; background: var(--mark-sky);
  }
  .brand-name {
    font-weight: 500; color: var(--mark-violet); letter-spacing: 2px;
  }
  .card--back .brand { left: 540px; top: 180px; }
  .card--back .brand-name { font-size: 54px; }
  .card--front .brand { left: 580px; top: 110px; }
  .card--front .brand-name { font-size: 46px; }

  /* Front side */
  .card--front { left: 340px; top: 510px; height: 470px; }
  .company {
    position: absolute; left: 55px; top: 48px;
    font-weight: 400; font-size: 30px; line-height: 36px; color: var(--ink);
  }
  .person { position: absolute; left: 52px; top: 232px; }
  .person-name {
    font-weight: 500; font-size: 34px; color: var(--name-blue); line-height: 38px;
  }
  .person-creds { font-weight: 500; font-size: 22px; color: var(--ink); margin-left: 4px; }
  .person-title { font-weight: 600; font-size: 16px; color: var(--ink); margin-left: 2px; line-height: 18px; }
  .contact {
    position: absolute; left: 53px; top: 326px; list-style: none;
    font-weight: 400; font-size: 17px; line-height: 22px; color: var(--contact-blue);
  }
  .services {
    position: absolute; right: 58px; top: 326px; width: 420px; text-align: right;
    font-weight: 300; font-size: 17px; line-height: 31px; color: var(--ink);
  }
</style>
</head>
<body>
<main class="canvas">
  <section class="card card--back" aria-label="Card back">
    <p class="back-statement">We are certified by the Baseline Ongoing Lawyer Instruction (BOLI) Panel of the Statewide High Tribunal to provide Continuing Legal Education (CLE) credits to Illinois attorneys.</p>
    <p class="back-call">Call about what courses we offer! (555) 214-0397</p>
    <div class="brand"><span class="brand-dot"></span><span class="brand-name">MCAC</span></div>
  </section>

  <section class="card card--front" aria-label="Card front">
    <h1 class="company">Meridel Clinical<br>Advising &amp; Coaching LLC</h1>
    <div class="brand"><span class="brand-dot"></span><span class="brand-name">MCAC</span></div>
    <div class="person">
      <p><span class="person-name">Danelle Brooks</span><span class="person-creds">M.S.W., LCSW</span></p>
      <p class="person-title">Clinical Therapist &amp; Trainer</p>
    </div>
    <ul class="contact">
      <li>helpdeskdanelle@mailbrook.example</li>
      <li>www.meridelclinicaladvising.example</li>
      <li>(555) 214-0397</li>
      <li>Halden, IL 60400</li>
    </ul>
    <p class="services">Providing clinical therapy services to<br>individuals, families, couples, and children.<br>We also provide life coaching and crisis training.</p>
  </section>
</main>
</body>
</html>
```